Gobal construction supply company needs new business card design

I need a business card design for my global supply company using an existing logo. i will be looking to print these on rounded corner cards with the black background version of my logo on the back. on the front white background, my logo again and my simple details.

```html
<!DOCTYPE html>
<html lang="en">
<head>
<meta charset="UTF-8">
<title>Meridian Build Supply — Business Card</title>
<link rel="stylesheet" href="https://fonts.googleapis.com/css2?family=Lexend:wght@500;600&family=Open+Sans:wght@400&display=swap">
<style>
  :root {
    --backdrop: #2d2d2f;
    --card-top: #1b1b1c;
    --card-bottom: #070707;
    --accent-red: #e00000;
    --text-white: #f2f2f2;
    --text-soft: #cfcfcf;
    --divider: #4a4a4a;
  }
  * { margin: 0; padding: 0; box-sizing: border-box; }
  html, body { width: 1200px; height: 900px; overflow: hidden; }
  body {
    background: var(--backdrop);
    display: flex;
    flex-direction: column;
    align-items: center;
    justify-content: center;
    gap: 44px;
    font-family: "Open Sans", Arial, sans-serif;
  }
  .card {
    position: relative;
    width: 580px;
    height: 330px;
    border-radius: 10px;
    overflow: hidden;
    background: linear-gradient(160deg, var(--card-top), var(--card-bottom));
    box-shadow: 0 10px 24px rgba(0,0,0,0.45);
  }
  .card__band {
    position: absolute;
    left: 0; right: 0; bottom: 0;
    height: 12px;
    background: var(--accent-red);
  }

  /* Back: brand */
  .card--back {
    display: flex;
    align-items: center;
    justify-content: center;
  }
  .brand {
    display: flex;
    align-items: center;
    gap: 14px;
    margin-bottom: 12px;
  }
  .brand__name {
    font-family: "Lexend", Arial, sans-serif;
    font-weight: 600;
    font-size: 28px;
    letter-spacing: 0.5px;
    color: var(--text-white);
    text-transform: uppercase;
  }
  .brand__dot {
    width: 18px; height: 18px;
    border-radius: 50%;
    background: var(--accent-red);
  }

  /* Front: details */
  .card--front {
    display: flex;
    align-items: center;
    padding-bottom: 12px;
  }
  .person {
    width: 292px;
    padding-right: 26px;
    text-align: right;
  }
  .person__name {
    font-family: "Lexend", Arial, sans-serif;
    font-weight: 500;
    font-size: 22px;
    letter-spacing: 0.5px;
    color: var(--accent-red);
    text-transform: uppercase;
  }
  .person__role {
    font-size: 16px;
    color: var(--text-soft);
    margin-top: 2px;
  }
  .divider {
    width: 1px;
    height: 96px;
    background: var(--divider);
  }
  .contacts {
    list-style: none;
    padding-left: 22px;
  }
  .contacts__item {
    display: flex;
    align-items: center;
    gap: 10px;
    font-size: 16px;
    line-height: 24px;
    color: var(--text-white);
  }
  .contacts__icon { width: 13px; height: 13px; flex: none; }
</style>
</head>
<body>

  <section class="card card--back" aria-label="Card back">
    <div class="brand">
      <span class="brand__name">Meridian Build Supply</span>
      <span class="brand__dot"></span>
    </div>
    <div class="card__band"></div>
  </section>

  <section class="card card--front" aria-label="Card front">
    <div class="person">
      <p class="person__name">Daniel Moore</p>
      <p class="person__role">Managing Director</p>
    </div>
    <div class="divider"></div>
    <ul class="contacts">
      <li class="contacts__item">
        <svg class="contacts__icon" viewBox="0 0 14 14"><path fill="#e00000" d="M1 4c0-2 1.5-3 3-3h6c1.5 0 3 1 3 3v1H9.5V3.8h-5V5H1zM3 6h8l2 6H1z"/><circle cx="7" cy="9" r="1.6" fill="#111"/></svg>
        <span>055-210 384 671</span>
      </li>
      <li class="contacts__item">
        <svg class="contacts__icon" viewBox="0 0 14 14"><rect x="3" y="0.5" width="8" height="13" rx="1.5" fill="none" stroke="#e00000" stroke-width="1.6"/><circle cx="7" cy="11" r="0.9" fill="#e00000"/></svg>
        <span>055-210 384 672</span>
      </li>
      <li class="contacts__item">
        <svg class="contacts__icon" viewBox="0 0 14 14"><rect x="0.5" y="2.5" width="13" height="9" rx="1" fill="#e00000"/><path d="M1 3l6 5 6-5" fill="none" stroke="#111" stroke-width="1.2"/></svg>
        <span>hello@meridianbuild.com</span>
      </li>
      <li class="contacts__item">
        <svg class="contacts__icon" viewBox="0 0 14 14"><circle cx="7" cy="7" r="6.5" fill="#e00000"/><path d="M0.5 7h13M7 0.5c-3 3-3 10 0 13M7 0.5c3 3 3 10 0 13" fill="none" stroke="#111" stroke-width="1"/></svg>
        <span>www.meridianbuild.com</span>
      </li>
    </ul>
    <div class="card__band"></div>
  </section>

</body>
</html>
```